Poster promoting concerts of the 20th anniversary season of the Hartwell Sonora Chamber Orchest

We need a poster (template) to promote the concert season and individual concerts of the Hartwell Sonora.
We present 8-10 programs avery season (oct - May)
the current info is on our website at www.thesonora-ens.org. Imagery from the website can be used for the design.
IMPORTANT DETAILS:
This season the orchestra will celebrate its 20th anniversary.
Poster must be printable in both color and black / white
Poster must be readable from a distance
Poster size is 11x17 inch
Website is NOT representative of the graphic design as we are looking to update the site after the poster is created.

Requirements
Must have
• Poster must be printable in both color and black / white
• Poster must be readable from a distance
• Poster size is 11x17 inch
Nice to have
• Please see the files for the soloists.

```html
<!DOCTYPE html>
<html lang="en">
<head>
<meta charset="utf-8">
<title>Hartwell Sonora – 20th Anniversary Season</title>
<link rel="stylesheet" href="https://fonts.googleapis.com/css2?family=Alegreya:ital,wght@1,400&family=Open+Sans&display=swap">
<style>
  :root {
    --sage-light: #d9dac6;
    --sage: #b9baa1;
    --sage-dark: #8f9079;
    --panel: #1a1a1a;
    --cream: #d6d6bd;
    --footer: #121212;
    --footer-text: #9a9a90;
    --wall-warm: #b4833f;
    --wall-deep: #8a6330;
    --stage-dark: #1f1a15;
  }
  * { margin: 0; padding: 0; box-sizing: border-box; }
  html, body { width: 777px; height: 1200px; overflow: hidden; background: var(--sage); }
  .poster {
    position: relative; width: 777px; height: 1200px; overflow: hidden;
    background: radial-gradient(ellipse at center, var(--sage-light) 50%, var(--sage) 80%, var(--sage-dark) 100%);
  }
  .pillar {
    position: absolute; top: 0; height: 1178px; width: 94px;
    background: repeating-linear-gradient(90deg,
      #c4c5ae 0 6px, #dcddc9 6px 14px, #b0b199 14px 18px, #cfd0ba 18px 30px);
  }
  .pillar--left { left: 0; }
  .pillar--right { right: 0; }
  .arch { position: absolute; left: 0; top: 0; }

  .ornament { position: absolute; }
  .ornament--crest {
    left: 312px; top: 44px; width: 150px; height: 138px;
    background: radial-gradient(ellipse at 50% 45%, rgba(214,214,189,.75) 0%, rgba(214,214,189,.35) 45%, rgba(214,214,189,0) 72%);
  }
  .ornament--corner {
    top: 118px; width: 56px; height: 140px;
    background: radial-gradient(ellipse at 50% 60%, rgba(214,214,189,.7) 0%, rgba(214,214,189,.3) 45%, rgba(214,214,189,0) 72%);
  }
  .ornament--corner-left { left: 94px; }
  .ornament--corner-right { left: 627px; }
  .ornament--side {
    top: 722px; width: 40px; height: 132px;
    background: radial-gradient(ellipse at 50% 55%, rgba(214,214,189,.7) 0%, rgba(214,214,189,.3) 45%, rgba(214,214,189,0) 72%);
  }
  .ornament--side-left { left: 94px; }
  .ornament--side-right { left: 643px; }

  .headline, .anniversary, .tagline, .season {
    position: absolute; left: 95px; width: 590px; text-align: center;
    color: var(--cream); font-family: "Alegreya", Georgia, serif; font-style: italic; font-weight: 400;
  }
  .headline { top: 222px; font-size: 80px; line-height: 90px; }
  .anniversary { top: 446px; font-size: 26px; padding-right: 40px; }
  .tagline { top: 543px; font-size: 39px; line-height: 48px; }
  .season { top: 664px; font-size: 25px; }

  .ensemble-photo {
    position: absolute; left: 95px; top: 830px; width: 590px; height: 348px;
    background:
      linear-gradient(180deg, var(--panel) 0%, rgba(26,26,26,.6) 6%, rgba(26,26,26,0) 14%),
      linear-gradient(90deg, rgba(0,0,0,.25) 0%, rgba(0,0,0,0) 20%, rgba(0,0,0,0) 80%, rgba(0,0,0,.25) 100%),
      linear-gradient(180deg, var(--wall-warm) 8%, var(--wall-deep) 38%, #4a3a28 55%, #2a231c 70%, var(--stage-dark) 100%);
  }
  .footer {
    position: absolute; left: 0; bottom: 0; width: 777px; height: 22px;
    background: var(--footer); color: var(--footer-text);
    font: 11px/22px "Open Sans", Arial, sans-serif; text-align: center;
  }
</style>
</head>
<body>
<main class="poster">
  <div class="pillar pillar--left"></div>
  <div class="pillar pillar--right"></div>

  <svg class="arch" width="777" height="1200" viewBox="0 0 777 1200" aria-hidden="true">
    <path d="M95,1178 V205 Q95,45 390,33 Q685,45 685,205 V1178 Z" fill="var(--panel)" stroke="var(--cream)" stroke-width="4"/>
  </svg>

  <div class="ornament ornament--crest" role="img" aria-label="Floral crest ornament"></div>
  <div class="ornament ornament--corner ornament--corner-left" role="img" aria-label="Scroll ornament"></div>
  <div class="ornament ornament--corner ornament--corner-right" role="img" aria-label="Scroll ornament"></div>
  <div class="ornament ornament--side ornament--side-left" role="img" aria-label="Leaf ornament"></div>
  <div class="ornament ornament--side ornament--side-right" role="img" aria-label="Leaf ornament"></div>

  <h1 class="headline">Hartwell<br>Sonora</h1>
  <p class="anniversary">20 th Anniversary</p>
  <p class="tagline">Come experiance the flow<br>of time through music.</p>
  <p class="season">8-10 programs every season (oct - May)</p>

  <div class="ensemble-photo" role="img" aria-label="Photograph of the chamber orchestra performing on stage with a conductor, warm wooden wall behind"></div>

  <footer class="footer">http://thesonora-ens.org/</footer>
</main>
</body>
</html>
```